Fresh Tarrow Work Post - Business Card Required

Dear All,

I own Velmira Limited, which in turn owns the website:
www.harbinworkpost.example

I want all of you wonderful creative people to come up with a slick, and awesome business card design that incorporates the logo on the site, and some colouring and design elements from it.

You have free reign in how you go about doing this, I won't be giving my contact details on this platform, but the winner will be asked to redesign based on my contact details which I will supply at the end.

I need the design to be completed within 5 days. I need the final print copies of the business cards by the 25th November, so unfortunately it's a bit of a rush to get these designs ready.

Any questions, please ask.

Thank you
Updates

Thank you all for your hard work and exceptional designs provided. I do have to pick one, so I have a very clear idea of which one this is, however I will wait one further day until the competition closes to be fair to all those have submitted, or are in the process of submitting. I wish you all the best and thank you again for your dedication.

```html
<!DOCTYPE html>
<html lang="en">
<head>
<meta charset="utf-8">
<title>Harbin Work Post – Business Card</title>
<link rel="stylesheet" href="https://fonts.googleapis.com/css2?family=Cinzel:wght@500&family=Exo+2:wght@400;600&display=swap">
<style>
  :root {
    --page-bg: #e4e4e4;
    --card-dark: #333232;
    --gold-light: #dcb764;
    --gold-mid: #c3974a;
    --gold-deep: #9c6f22;
    --name-white: #ffffff;
    --contact-ink: #3a2a12;
  }
  * { margin: 0; padding: 0; box-sizing: border-box; }
  html, body {
    width: 1200px; height: 900px; overflow: hidden;
    background: var(--page-bg);
  }
  .card {
    position: absolute; left: 100px; top: 164px;
    width: 1000px; height: 572px;
    background: var(--card-dark);
    overflow: hidden;
    box-shadow: 0 14px 30px rgba(0,0,0,0.25);
  }
  .card__gold-area {
    position: absolute; inset: 0;
    background: radial-gradient(ellipse at 60% 55%, var(--gold-light) 0%, var(--gold-mid) 55%, var(--gold-deep) 100%);
    clip-path: polygon(640px 0, 1000px 0, 1000px 572px, 400px 572px);
  }
  .brand {
    position: absolute; left: 70px; top: 170px;
    font-family: "Cinzel", serif; font-weight: 500;
    font-size: 34px; letter-spacing: 3px;
    color: var(--gold-mid);
  }
  .brand__rule {
    position: absolute; left: 70px; top: 222px;
    width: 300px; height: 2px; background: var(--gold-mid);
  }
  .holder {
    position: absolute; left: 70px; top: 270px;
    font-family: "Exo 2", sans-serif; color: var(--name-white);
  }
  .holder__name { font-weight: 600; font-size: 34px; letter-spacing: 1.5px; }
  .holder__role { font-weight: 400; font-size: 22px; margin-top: 2px; padding-left: 40px; }
  .contact {
    position: absolute; right: 44px; top: 60px;
    font-family: "Exo 2", sans-serif; font-size: 17px;
    color: var(--contact-ink); text-align: right; line-height: 1.45;
    list-style: none;
  }
  .contact__item { display: flex; justify-content: flex-end; align-items: flex-start; gap: 10px; }
  .contact__item + .contact__item { margin-top: 8px; }
  .contact__icon { width: 16px; height: 16px; flex: none; margin-top: 4px; }
</style>
</head>
<body>
  <article class="card">
    <div class="card__gold-area" role="img" aria-label="Gold decorative wave panel"></div>

    <div class="brand">Harbin Work Post</div>
    <div class="brand__rule"></div>

    <div class="holder">
      <div class="holder__name">MARCUS HALLDEN</div>
      <div class="holder__role">Managing Director</div>
    </div>

    <ul class="contact">
      <li class="contact__item">
        <span>041 9th floor Court<br>Brenlow Road QTR</span>
        <svg class="contact__icon" viewBox="0 0 16 16"><path d="M8 1a5 5 0 0 0-5 5c0 4 5 9 5 9s5-5 5-9a5 5 0 0 0-5-5zm0 7a2 2 0 1 1 0-4 2 2 0 0 1 0 4z" fill="var(--contact-ink)"/></svg>
      </li>
      <li class="contact__item">
        <span>020 555 0147</span>
        <svg class="contact__icon" viewBox="0 0 16 16"><path d="M3 1h3l1.5 4-2 1.2a9 9 0 0 0 4.3 4.3L11 8.5l4 1.5v3a2 2 0 0 1-2 2A12 12 0 0 1 1 3a2 2 0 0 1 2-2z" fill="var(--contact-ink)"/></svg>
      </li>
      <li class="contact__item">
        <span>020 555 0148</span>
        <svg class="contact__icon" viewBox="0 0 16 16"><rect x="4" y="1" width="8" height="14" rx="1.5" fill="none" stroke="var(--contact-ink)" stroke-width="1.6"/><circle cx="8" cy="12.5" r="0.9" fill="var(--contact-ink)"/></svg>
      </li>
      <li class="contact__item">
        <span>desk@harbinpost.example</span>
        <svg class="contact__icon" viewBox="0 0 16 16"><rect x="1" y="3" width="14" height="10" rx="1" fill="var(--contact-ink)"/><path d="M1.5 3.5 8 9l6.5-5.5" fill="none" stroke="var(--gold-mid)" stroke-width="1.3"/></svg>
      </li>
      <li class="contact__item">
        <span>www.harbinworkpost.example</span>
        <svg class="contact__icon" viewBox="0 0 16 16"><circle cx="8" cy="8" r="6.5" fill="none" stroke="var(--contact-ink)" stroke-width="1.5"/><path d="M1.5 8h13M8 1.5c-3 3.5-3 9.5 0 13M8 1.5c3 3.5 3 9.5 0 13" fill="none" stroke="var(--contact-ink)" stroke-width="1.1"/></svg>
      </li>
    </ul>
  </article>
</body>
</html>
```